Flyer-Design für Apotheke
Zielgruppe
Wir sind eine Apotheke, mit Schwerpunkt Mutter-Kind / Wiegenhafen Apotheke (www.wiegenhafen Apotheke)
Zielgruppe: Wir haben uns zertifiziert und spezialisiert im Bereich Mütter / Kinderwunsch / Stillen / Babys etc. (Siehe Anbei unser aktueller Entwurf Mutter-Kind-Broschüre)
Wir haben zahlreiche Handouts zu spezifischen Themen von der LHTV und unserem Verein Wiegenhafen Apotheken für unser Kunden schon fertig gestellt (siehe ein Beispiel im Anhang, auf dem wir noch unser Logo eingefügt haben).
Die Handouts sind meist 4-seitig A5, im Anhang mit unserem Logo noch versehen.
Zu zwei Themen möchten wir jetzt noch selbst ein Handout erstellen.
1) Fieberthermometer
2) Schnuller
Ziel: 4-6 Seiten, wir wollen es dann bei Druckfuchs drucken lassen.
Zielgruppe: Mütter, die zu uns in die Apotheke kommen und beraten werden (konkret in diesen Beispielen zum Thema Fieberthermometer bzw. Schnuller. Damit sie was mit nach Hause nehmen können, möchten wir die Handouts erstellen.
Texte anbei, Graphische Umsetzung ggf. mit netten Baby/Mütterbildern o.ä. erwünscht
Aufgabenstellung
Einbau Logo Tolvena-Apotheke (siehe Anhang) ähnlich wie auf dem Flyer Ernährung
(als Logo ohne Adresse etc. und irgendwo unter mit Adresse, Telefon etc.)
Logo Wiegenhafen Apotheke DARF NICHT MIT DRAUF

```html
<!DOCTYPE html>
<html lang="de">
<head>
<meta charset="utf-8">
<title>Informationsbroschüre Schnuller &amp; Fieberthermometer</title>
<link rel="stylesheet" href="https://fonts.googleapis.com/css2?family=Open+Sans:wght@400;600;700&display=swap">
<style>
  :root{
    --teal:#138a7c;
    --teal-dark:#0d6f68;
    --teal-light:#2aa394;
    --box:#e4f2fb;
    --box-line:#9cc7e2;
    --ink:#2b2b2b;
    --grey:#7c7c7c;
    --red:#d0202a;
    --stage:#e8e8e8;
    --paper:#ffffff;
  }
  *{box-sizing:border-box;margin:0;padding:0}
  html,body{width:1200px;height:900px;overflow:hidden}
  body{background:var(--stage);font-family:"Open Sans",Arial,sans-serif;color:var(--ink);position:relative}
  .page{position:absolute;top:181px;width:380px;height:537px;background:var(--paper);box-shadow:0 4px 14px rgba(0,0,0,.18);overflow:hidden}

  /* Cover */
  .cover{left:24px}
  .cover-photo{position:absolute;left:0;top:70px;width:100%;height:467px;
    background:linear-gradient(150deg,#8f8a55 0%,#b9a96e 30%,#d8c9b0 55%,#a0785c 80%,#c9b39a 100%)}
  .cover-panel{position:absolute;inset:0;top:70px;background:linear-gradient(160deg,var(--teal-dark),var(--teal-light));
    clip-path:polygon(0 0,38% 0,96% 100%,0 100%)}
  .brand{position:absolute;display:flex;align-items:center;gap:5px;font-weight:700;color:var(--teal-dark);font-size:13px}
  .brand .dot{width:8px;height:8px;border-radius:50%;background:var(--red)}
  .cover .brand{right:22px;top:26px}
  .cover-title{position:absolute;left:22px;top:150px;width:230px;color:#fff;font-variant:small-caps;font-weight:400;font-size:23px;line-height:1.05;letter-spacing:.5px}
  .cover-title .small{font-size:16px}
  .cover-sub{position:absolute;left:22px;top:318px;color:#fff;font-size:13px;letter-spacing:.3px}
  .cover-contact{position:absolute;left:22px;bottom:22px;color:#fff;font-size:7.5px;line-height:1.5}
  .cover-contact .name{font-size:14px;font-weight:700;margin-bottom:4px;display:flex;align-items:center;gap:5px}
  .cover-contact .name .dot{width:8px;height:8px;border-radius:50%;background:#fff}
  .cover-contact .web{color:#ffd2d2;font-weight:700;font-size:10px}
  .cover-contact .fine{opacity:.8;font-size:6px;margin-top:3px}

  /* Inner spread */
  .inner-left{left:416px;box-shadow:-2px 4px 14px rgba(0,0,0,.18)}
  .inner-right{left:796px;border-left:1px solid #ddd}
  .inner{padding:34px 26px 0 26px;font-size:7.4px;line-height:1.45}
  .inner .brand{right:24px;top:22px;font-size:11px}
  .inner h1{font-variant:small-caps;font-weight:400;font-size:15px;letter-spacing:.4px;margin-top:40px;margin-bottom:8px}
  .lead{color:var(--grey);margin-bottom:8px}
  .label{color:var(--grey);font-size:9px;margin:8px 0 4px}
  .label.big{font-size:10.5px;color:#555}
  .box{background:var(--box);border:1px solid var(--box-line);padding:6px 9px;list-style:none}
  .box li{padding-left:7px;position:relative}
  .box li::before{content:"•";position:absolute;left:0}
  .note{color:var(--grey);margin-top:8px}
  .closing{color:var(--grey);margin-top:14px;font-size:8px;line-height:1.7}
  .footer{position:absolute;left:26px;right:26px;bottom:16px;font-size:5.5px;color:var(--grey);display:flex;justify-content:space-between;gap:12px}
  .footer span:last-child{white-space:nowrap}
  .inner-right .box:first-child{margin-top:30px}
</style>
</head>
<body>

<section class="page cover">
  <div class="brand"><span class="dot"></span>Tolvena-Apotheke</div>
  <div class="cover-photo" role="img" aria-label="Foto einer schwangeren Frau im weißen Kleid auf einem sonnigen Waldweg"></div>
  <div class="cover-panel"></div>
  <h1 class="cover-title">Der Schnuller -<br><span class="small">ja oder nein?</span><br><span class="small">und</span><br>Gewusst, wie! - Fieber-<br>Thermometer<br>und - Messung</h1>
  <p class="cover-sub">Informationsbroschüre</p>
  <div class="cover-contact">
    <div class="name"><span class="dot"></span>Tolvena-Apotheke</div>
    <div>Lindenhofstraße 8 - 47113 Kesselbach - Tel. 09876 / 54 32 10</div>
    <div class="web">www.tolvena-apotheke.de</div>
    <div class="fine">Die vorliegenden Informationen ersetzen keine persönliche Beratung.<br>www.wiegenhafen-apotheke.de</div>
  </div>
</section>

<section class="page inner inner-left">
  <div class="brand"><span class="dot"></span>Tolvena-Apotheke</div>
  <h1>Der Schnuller - ja oder nein?</h1>
  <p class="lead">Der Einsatz von Schnullern wird kontrovers diskutiert. Die Entscheidung, ob Sie Ihrem Kind einen Beruhigungssauger geben oder nicht, liegt bei Ihnen.</p>
  <p class="label">Das spricht dafür:</p>
  <ul class="box">
    <li>Zur Beruhigung des Säuglings vor allem bei Trennung von Mutter und Kind</li>
    <li>ABER: Brust und Daumen sind Ersatz für Ruhe und Saugbedürfnis zu stillen</li>
    <li>Vorteilhafte Auswirkung auf den Saug- und Schluckreflex bei Frühgeborenen</li>
    <li>Protektiver Effekt auf den plötzlichen Kindstod durch regelmäßigen Gebrauch zum Einschlafen</li>
  </ul>
  <p class="label">Das spricht dagegen:</p>
  <ul class="box">
    <li>Hungerzeichen des Kindes werden leichter übersehen</li>
    <li>Mögliche verminderte Milchbildung durch zu seltenes Anlegen an der Brust</li>
    <li>Nur Brust passt sich optimal an kindlichen Mund an, auch kieferechte Sauger erfüllen Voraussetzungen nicht</li>
    <li>Saugen am Schnuller erfolgt mit anderen Bewegungen als an der Brust</li>
    <li>Mögliche Irritationen beim Trinken</li>
    <li>Zunge liegt nicht in der normalen Ruheposition</li>
    <li>Kann Störungen im Mundraum (Sprechstörungen, Zahn- und Kieferfehlstellungen etc.) begünstigen</li>
  </ul>
  <p class="note">Egal ob Sie sich dafür oder dagegen entscheiden, wichtig ist in jedem Fall ein verantwortungsbewusster und achtsamer Einsatz des Schnullers.</p>
  <p class="label big">Anforderungen an den Schnuller:</p>
  <ul class="box">
    <li>Möglichst niedriger Schnullerschaft → Schneidezähne werden beim Wachstum nicht gehindert</li>
    <li>Raumsparendes und angepasstes Lutschteil → Vermeidung der Entstehung von zu engen oder kleinen Oberkiefern</li>
    <li>Achtung: Kirschsauger verhindern den Mundschluss, daher nicht empfehlenswert.</li>
  </ul>
  <div class="footer"><span>Die vorliegenden Informationen wurden mit größtmöglicher Sorgfalt erstellt und ersetzen keine ärztliche Beratung. Stand der Angaben bei Drucklegung.</span><span>Seite 2</span></div>
</section>

<section class="page inner inner-right">
  <ul class="box">
    <li>Möglichst flexibles, weiches und bewegliches Lutschteil → mehr Raum für die Zunge als Gaumen- und Kieferformer</li>
    <li>Tipp: Latex ist weicher als Silikon</li>
    <li>Möglichst leichter Schnuller → keine Überforderung der Lippen- und Zungenmuskulatur</li>
    <li>Achtung: Schnullerkette erhöht das Gewicht zusätzlich</li>
    <li>Schnuller muss nicht mitwachsen → Brustwarze verändert sich auch nicht</li>
    <li>Zunge braucht wachsenden Freiraum für Sprachentwicklung</li>
    <li>Beruhigungssauger sollte keine Geschmacks- und Zusatzstoffe, sowie gesundheitsschädliche Chemikalien enthalten</li>
  </ul>
  <p class="label big">Wertvolle Tipps beim Umgang mit dem Beruhigungssauger:</p>
  <ul class="box">
    <li>In den ersten 4-6 Wochen möglichst den Gebrauch vermeiden, um die Milchproduktion optimal anlaufen zu lassen</li>
    <li>Schnuller ist kein Ersatz für engen Körperkontakt und Stillen</li>
    <li>Kein Dauergebrauch, nur kurzzeitige Anwendung</li>
    <li>Falls Schnuller beim Schlafen herausfällt, nicht wieder zurück in den Mund schieben</li>
    <li>Schnuller nicht herumliegen lassen, so wird das Kind dazu verleitet</li>
    <li>Sprechen ohne Beruhigungssauger</li>
    <li>Ab dem 2. Lebensjahr mit dem Abgewöhnen beginnen</li>
    <li>Auf hygienischen Umgang achten</li>
  </ul>
  <p class="closing">Bei weiteren Fragen helfen wir Ihnen gerne weiter.<br>Ihr babyfreundliches Team der Tolvena Apotheke Kesselbach</p>
  <div class="footer"><span>Die vorliegenden Informationen wurden sorgfältig geprüft und ersetzen keine persönliche Beratung durch Arzt, Hebamme oder Apotheke.</span><span>Seite 3</span></div>
</section>

</body>
</html>
```